Window Treatment business needs website redesigned.

We need a revamp and refresh of our current site www.velmorin.ca
Looking to attract very high end customer. It should be a very simple design with very little text. This site will be visited by prospective homeowners, designers, builders and architects. They should feel that they are dealing with a high-end product selection, where experience, customer service and unique product offering is the focus. The content will be to highlight our services and highlight the manufacturers we sell, using a few rich photos to highlight the products. We should NOT look like we are a very large company. It should NOT have discounts/savings buttons and many menus to choose from. We offer over 15 years experience to narrow the many market options, to provide the right technical solution.
We specialize in products that are not readily available on the market and specifically motorized systems for indoors and outdoors.
Our main suppliers are Quarnel.com, Dexavo.com
We carry our own locally manufactured product line of roller shades.
Main product pictures should be of roller shades, outdoor bug screens, awnings and outdoor pergolas.

Reason: I understand that Christmas is coming up real short and many people are extremely busy. If you have a CREATIVE gifting you still want to submit, I look forward to your idea!

Reason: Due to holiday season, we have not had sufficient time to review to make a final decision. Thank you for your patience!

Target Market(s)

High end home owners, designers, builders, architects

Industry/Entity Type

Contractor

Coding

Coded - Design and coding required

Number of Pages Required

3 page

Font styles to use
Sans Serif

Requirements
Must have
• Landing page with full size image like homepage of borvela.it
• Products page that highlights products with simple product shot image, description and link to manufacturer.
• On main page a scrolling of customer reviews.
• I want a very simple, eye-catching, emotional image for homepage. It does not need to include any product image.
• An image that shows technology combining/meshing with hand craftsmanship.
• Focus is on design.
• http://www.borvela.it/en/gallery is a great layout and design.
Nice to have
• Logo shape for icons and watermark should be used.
• Look like and have simple motion effects like tirquel.com or manvexo.com
Should not have
• Generic/standard looking feel like gostrel.com or plinkwardcove.ca
• No use of green as background only subtle text.
• Lots of text and pages.

```html
<!DOCTYPE html>
<html lang="en">
<head>
<meta charset="utf-8">
<title>Velmorin — Window Treatment Solutions</title>
<link rel="stylesheet" href="https://fonts.googleapis.com/css2?family=Open+Sans:wght@300;400;600;700;800&display=swap">
<style>
:root{
  --accent:#5dba47;
  --ink:#222;
  --charcoal:#2a2a2a;
  --stone:#c4c4c4;
  --stone-dark:#9e9e9e;
  --panel:#f4f4f4;
  --footer:#1c1c1c;
  --white:#fff;
}
*{box-sizing:border-box;margin:0;padding:0}
html,body{width:1200px;height:3125px;overflow:hidden;background:var(--white)}
body{position:relative;font-family:"Open Sans",Arial,sans-serif;color:var(--ink)}
.abs{position:absolute}

/* hero */
.hero{left:0;top:0;width:1200px;height:792px;background:linear-gradient(180deg,#dfe9f3 0%,#b9cde0 30%,#e4e8ec 55%,#8f9c84 80%,#6f7e66 100%)}
.masthead{left:0;top:0;width:1200px;height:135px;background:rgba(235,240,246,.55)}
.brand{left:73px;top:30px;display:flex;align-items:center;gap:10px}
.brand-mark{width:56px;height:56px;border-radius:50%;background:var(--charcoal)}
.brand-name{font-size:36px;font-weight:600;color:var(--ink);line-height:1}
.brand-tag{left:139px;top:74px;font-size:13px;color:var(--ink)}
.nav{left:654px;top:0;display:flex;font-size:13px;font-weight:600;text-transform:uppercase}
.nav a{color:var(--ink);text-decoration:none;height:80px;display:flex;align-items:center;padding:0 13px}
.nav .current{background:var(--white);color:var(--accent);border-bottom:3px solid var(--accent);padding:0 10px}
.search{left:856px;top:96px;width:269px;height:27px;border:2px solid #333;background:rgba(255,255,255,.6);font-size:12px;padding:4px 10px}
.search svg{position:absolute;right:8px;top:4px}
.arrow{width:42px;height:42px;border-radius:50%;background:rgba(30,30,30,.75);top:433px;display:flex;align-items:center;justify-content:center}

/* feature cards */
.card{top:638px;width:304px}
.card-text{height:154px;background:var(--white);text-align:center;padding:20px 22px 0}
.card-title{color:var(--accent);font-weight:700;font-size:16px;margin-bottom:10px}
.card-text p{font-size:12.5px;line-height:1.45}
.card-photo{height:204px;display:flex;align-items:center;justify-content:center}
.ring{width:40px;height:40px;border-radius:50%;border:2px solid rgba(255,255,255,.85)}
.ring-small{width:30px;height:30px;border-radius:50%;border:2px solid var(--accent)}

/* welcome */
.welcome-photo{left:73px;top:1160px;width:512px;height:317px;border:4px solid #111;background:linear-gradient(160deg,#cfd8df,#7d8b93 60%,#4d5a5f)}
.h-light{color:var(--accent);font-weight:300;font-size:62px;line-height:1}
.copy{font-size:13.5px;line-height:1.4;text-align:justify}

/* services */
.h-bold{color:var(--accent);font-weight:800;letter-spacing:.5px;line-height:1}
.social-box{left:73px;top:1820px;width:317px;height:409px;background:var(--charcoal);color:var(--white);padding:20px 16px}
.social-box h3{font-weight:400;font-size:17px;line-height:1.3}
.social-box p{font-size:13.5px;line-height:1.35;margin-top:12px}
.dots{display:flex;gap:9px;margin-top:16px}
.dots span{width:33px;height:33px;border-radius:50%;background:#555}
.subscribe{display:flex;margin-top:22px;height:41px;gap:13px}
.subscribe .field{width:187px;background:#444;font-size:13px;padding:11px 16px}
.subscribe .btn{width:91px;background:var(--white);color:var(--ink);font-size:13px;padding:11px 28px}

/* order & contact */
.video{left:73px;top:2365px;width:452px;height:215px;background:linear-gradient(120deg,#1b2a4a,#2e5a93 55%,#0f1c33);border-top:10px solid #111}
.contact{left:679px;top:2365px;width:448px;height:475px;background:var(--panel);padding:17px 25px}
.contact h2{font-size:34px;font-weight:400;color:var(--accent);line-height:1}
.contact p{font-size:13px;line-height:1.35;margin-top:14px}
.input{left:704px;width:394px;height:55px;background:var(--white);font-size:13px;padding:18px 12px}
.submit{left:1008px;top:2792px;width:90px;height:27px;background:var(--charcoal);color:var(--white);font-weight:700;font-size:14px;text-align:center;line-height:27px}

/* footer */
.footer{left:0;top:2910px;width:1200px;height:215px;background:var(--footer);color:var(--white);text-align:center}
.footer h2{font-size:40px;font-weight:700;margin-top:30px}
.footer .legal{font-size:14px;margin-top:8px}
.footer .legal em{color:var(--accent);font-style:normal}
.footer .links{display:flex;justify-content:center;gap:38px;margin-top:26px}
.footer .links span{width:36px;height:36px;border-radius:50%;background:var(--white)}
</style>
</head>
<body>

<section class="abs hero" role="img" aria-label="Photograph of a modern two-storey white villa with palm trees under a blue sky"></section>

<header class="abs masthead"></header>
<div class="abs brand"><span class="brand-mark"></span><span class="brand-name">Velmorin</span></div>
<div class="abs brand-tag">Window Treatment Solutions</div>
<nav class="abs nav">
  <a class="current">Home</a><a>About</a><a>Services</a><a>Projects</a><a>Blog</a><a>Contacts</a>
</nav>
<div class="abs search">Search ...
  <svg width="18" height="18" viewBox="0 0 18 18"><circle cx="7" cy="7" r="5" fill="none" stroke="#222" stroke-width="2"/><line x1="11" y1="11" x2="16" y2="16" stroke="#222" stroke-width="2.5"/></svg>
</div>
<div class="abs arrow" style="left:8px"><svg width="14" height="16"><path d="M11 2 L4 8 L11 14" fill="none" stroke="#fff" stroke-width="3"/></svg></div>
<div class="abs arrow" style="left:1148px"><svg width="14" height="16"><path d="M3 2 L10 8 L3 14" fill="none" stroke="#fff" stroke-width="3"/></svg></div>

<article class="abs card" style="left:75px">
  <div class="card-text"><h3 class="card-title">WINDOW-FACADE</h3>
  <p>Motorized exterior roller shades that keep heat out and the view in, fitted to each opening with care.</p></div>
  <div class="card-photo" role="img" aria-label="Glass facade with exterior shade in sunlight" style="background:linear-gradient(160deg,#5b7390,#2d3c52)"><span class="ring"></span></div>
</article>
<article class="abs card" style="left:448px">
  <div class="card-text"><h3 class="card-title">BALCONY &amp; TERRACE</h3>
  <p>Retractable bug screens and awnings that turn a terrace into a calm outdoor room, day or night.</p></div>
  <div class="card-photo" role="img" aria-label="Terrace with glass roof and shading system" style="background:linear-gradient(160deg,#6c7478,#3d4448)"><span class="ring"></span></div>
</article>
<article class="abs card" style="left:821px">
  <div class="card-text"><h3 class="card-title">FLOOR &amp; OPEN SPACES</h3>
  <p>Louvred pergolas with quiet motors and hidden drives, built to last through every season.</p></div>
  <div class="card-photo" role="img" aria-label="Open patio under a retractable pergola" style="background:linear-gradient(160deg,#7a6a58,#3f3a33)"><span class="ring"></span></div>
</article>

<div class="abs welcome-photo" role="img" aria-label="Apartment balconies fitted with exterior roller screens"></div>
<h1 class="abs h-light" style="left:610px;top:1188px">WELCOME</h1>
<p class="abs copy" style="left:610px;top:1283px;width:518px">For over fifteen years we have helped homeowners, designers, builders and architects choose the right shading for each project. We narrow a crowded market to a few products that are not readily found elsewhere, with a focus on motorized systems for indoors and outdoors, and our own locally made line of roller shades. Every install is measured, fitted and looked after by the same small team.</p>
<span class="abs ring-small" style="left:614px;top:1405px"></span>

<h2 class="abs h-bold" style="left:73px;top:1640px;font-size:34px">SERVICES</h2>
<p class="abs copy" style="left:73px;top:1696px;width:317px">From first sketch to final fitting, we advise on the right technical solution and install it with care.</p>
<span class="abs ring-small" style="left:73px;top:1770px;width:26px;height:26px"></span>

<aside class="abs social-box">
  <h3>Follow our latest projects on social networks</h3>
  <p>See recent homes, terraces and facades we have fitted, and new products as they arrive.</p>
  <div class="dots"><span></span><span></span><span></span><span></span></div>
  <h3 style="margin-top:46px">Sign up for updates</h3>
  <p>Leave your email and we will share new projects and product news a few times a year.</p>
  <div class="subscribe"><span class="field">Your e-mail</span><span class="btn">Get</span></div>
</aside>

<svg class="abs" style="left:558px;top:1660px" width="570" height="570" viewBox="0 0 570 570" font-family="Open Sans, Arial, sans-serif">
  <g font-weight="700" font-size="15" fill="#fff" text-anchor="middle">
    <polygon points="83,0 201,0 284,83 284,201 201,284 83,284 0,201 0,83" fill="#9e9e9e"/>
    <polygon points="369,0 487,0 570,83 570,201 487,284 369,284 286,201 286,83" fill="#c4c4c4"/>
    <polygon points="83,286 201,286 284,369 284,487 201,570 83,570 0,487 0,369" fill="#c4c4c4"/>
    <polygon points="369,286 487,286 570,369 570,487 487,570 369,570 286,487 286,369" fill="#9e9e9e"/>
    <text x="142" y="88">Roller Shades</text>
    <text x="428" y="88">Bug Screens</text>
    <text x="142" y="374">Awnings</text>
    <text x="428" y="374">Pergolas</text>
  </g>
  <!-- roller shade -->
  <rect x="102" y="118" width="80" height="12" rx="6" fill="#fff"/>
  <rect x="108" y="130" width="68" height="50" fill="#fff" opacity=".85"/>
  <rect x="104" y="180" width="76" height="6" fill="#fff"/>
  <!-- screen -->
  <rect x="388" y="118" width="80" height="68" fill="none" stroke="#fff" stroke-width="4"/>
  <g stroke="#fff" stroke-width="1.5"><line x1="388" y1="135" x2="468" y2="135"/><line x1="388" y1="152" x2="468" y2="152"/><line x1="388" y1="169" x2="468" y2="169"/><line x1="408" y1="118" x2="408" y2="186"/><line x1="428" y1="118" x2="428" y2="186"/><line x1="448" y1="118" x2="448" y2="186"/></g>
  <!-- awning -->
  <rect x="100" y="402" width="84" height="8" fill="#fff"/>
  <path d="M102 410 L182 410 L196 448 L88 448 Z" fill="#fff"/>
  <g stroke="#c4c4c4" stroke-width="3"><line x1="120" y1="412" x2="112" y2="446"/><line x1="142" y1="412" x2="142" y2="446"/><line x1="164" y1="412" x2="172" y2="446"/></g>
  <!-- pergola -->
  <rect x="384" y="400" width="88" height="10" fill="#fff"/>
  <g fill="#fff"><rect x="390" y="410" width="6" height="60"/><rect x="460" y="410" width="6" height="60"/></g>
  <g stroke="#fff" stroke-width="3"><line x1="384" y1="418" x2="472" y2="418"/><line x1="384" y1="426" x2="472" y2="426"/><line x1="384" y1="434" x2="472" y2="434"/></g>
  <!-- centre -->
  <polygon points="285,190 380,285 285,380 190,285" fill="#1c1c1c"/>
  <text x="285" y="288" fill="#fff" font-weight="700" font-size="24" text-anchor="middle">SERVICES</text>
  <circle cx="285" cy="313" r="12" fill="none" stroke="#fff" stroke-width="2"/>
</svg>

<div class="abs video" role="img" aria-label="Video preview of a motorized shade installation"></div>
<h2 class="abs h-bold" style="left:73px;top:2636px;font-size:50px">MAKE AN ORDER</h2>
<p class="abs copy" style="left:73px;top:2709px;width:452px">Tell us about your space and we will arrange a visit to measure and advise. Each order is made to fit, with a clear quote, a set install date and service after the work is done.</p>
<span class="abs ring-small" style="left:73px;top:2796px;width:26px;height:26px"></span>

<section class="abs contact">
  <h2>CONTACT US</h2>
  <p>Send a few details about your project and we will reply within one working day to book a consultation.</p>
</section>
<div class="abs input" style="top:2513px">Name</div>
<div class="abs input" style="top:2583px">E-mail</div>
<div class="abs input" style="top:2652px">Phone</div>
<div class="abs input" style="top:2723px">Message</div>
<div class="abs submit">SUBMIT</div>

<footer class="abs footer">
  <h2>copyright</h2>
  <div class="legal">Velmorin <em>© 2016</em> Privacy Policy</div>
  <div class="links"><span></span><span></span><span></span><span></span><span></span><span></span></div>
</footer>

</body>
</html>
```